Create Print and Packaging Designs for Copper Fern Tea Company

Develop a contemporary design for Copper Fern Tea Company tea boxes that will be extended to logo, website, banners and define corporate identity. The package design should represent a fresh, spring, clean design that visually represents a modern view of tea drinking.

Logo and branding should include a daisy. Design should also be presented in 8-10 different palette themes to represent 8-10 different tea products. Packaging dimensions will approximately be 2.5"wx3.5h"x5.5"l with shoe box type lid having rear attached to main box

Teas include Black, Green, White, Oolong, Herbal & Decaf.

Future work based on quality and skills identified in winning entry.

I will need all source images for winning entry in gif, jpeg formats

```html
<!DOCTYPE html>
<html lang="en">
<head>
<meta charset="utf-8">
<title>Copper Fern Tea Company – Black Tea Box</title>
<link rel="stylesheet" href="https://fonts.googleapis.com/css2?family=Open+Sans:ital,wght@0,400;0,600;1,400&display=swap">
<style>
  :root {
    --stage: #e6e7e9;
    --paper: #f4f4f5;
    --paper-side: #eeeeef;
    --teal: #2a95ad;
    --ink: #6d7073;
    --ink-soft: #9a9da0;
    --shape: #8a8c8f;
    --photo-light: #e9ede4;
    --photo-mid: #a9b99a;
    --photo-deep: #6f8a5c;
    --decor: #e4e5e7;
  }
  html, body {
    margin: 0;
    width: 1200px;
    height: 1200px;
    overflow: hidden;
    background: var(--stage);
    font-family: "Open Sans", Arial, sans-serif;
  }
  .dieline {
    position: absolute;
    left: 190px;
    top: 130px;
    width: 820px;
    height: 940px;
    display: flex;
  }
  .panel {
    position: relative;
    height: 940px;
    overflow: hidden;
  }
  .panel--side { width: 280px; background: var(--paper-side); }
  .panel--front { width: 540px; background: var(--paper); }

  /* shared bottom zone */
  .rule {
    position: absolute;
    left: 0; right: 0;
    height: 2px;
    background: var(--teal);
  }
  .rule--upper { top: 590px; }
  .rule--lower { top: 650px; }
  .band {
    position: absolute;
    left: 0; right: 0;
    top: 670px;
    height: 40px;
    background: var(--teal);
  }
  .footer-line {
    position: absolute;
    left: 0; right: 0;
    top: 608px;
    text-align: center;
    color: var(--teal);
    font-size: 17px;
    letter-spacing: 0.5px;
  }
  .slogan {
    font-weight: 600;
    letter-spacing: 2px;
    text-transform: uppercase;
  }
  .meadow {
    position: absolute;
    left: 190px;
    top: 840px;
    width: 820px;
    height: 230px;
    background: linear-gradient(180deg, var(--photo-light) 0%, var(--photo-mid) 55%, var(--photo-deep) 100%);
  }

  /* side panel content */
  .side-copy {
    position: absolute;
    left: 26px; right: 24px;
    top: 34px;
    color: var(--ink);
    font-size: 10.5px;
    line-height: 1.55;
  }
  .side-copy h2 {
    margin: 0 0 14px;
    color: var(--teal);
    font-size: 12.5px;
    font-weight: 400;
    font-style: italic;
    line-height: 1.35;
  }
  .side-copy p { margin: 0 0 14px; }
  .features {
    margin: 0 0 18px;
    padding: 0;
    list-style: none;
    color: var(--teal);
    font-size: 11px;
  }
  .features li::before { content: "- "; }
  .sponsors-label {
    text-align: center;
    color: var(--teal);
    font-size: 11px;
    margin-bottom: 10px;
  }
  .sponsors {
    display: flex;
    justify-content: center;
    gap: 22px;
    margin-bottom: 14px;
  }
  .sponsor { width: 26px; height: 26px; background: var(--shape); }
  .sponsor--round { border-radius: 50%; }
  .fine-print {
    text-align: center;
    font-size: 9px;
    color: var(--ink-soft);
  }

  /* front panel content */
  .cup-mark {
    position: absolute;
    left: 28px; top: 26px;
    width: 60px;
    text-align: center;
    color: var(--ink-soft);
    font-size: 9px;
  }
  .brand {
    position: absolute;
    left: 200px; right: 30px;
    top: 78px;
    display: flex;
    align-items: center;
    gap: 12px;
    color: var(--teal);
    font-size: 30px;
    font-weight: 600;
    line-height: 1.1;
  }
  .brand-dot {
    flex: none;
    width: 18px; height: 18px;
    border-radius: 50%;
    background: var(--teal);
  }
  .variety {
    position: absolute;
    left: 0; top: 170px;
    width: 200px; height: 96px;
    box-sizing: border-box;
    padding: 18px 0 0 24px;
    background: var(--teal);
    color: #fff;
    font-size: 19px;
    line-height: 1.3;
  }
  .photo-window {
    position: absolute;
    left: 75px; top: 280px;
    width: 405px; height: 230px;
    background: linear-gradient(135deg, var(--photo-light) 0%, var(--photo-mid) 50%, var(--photo-deep) 100%);
  }
  .corner-decor {
    position: absolute;
    left: 470px; top: 420px;
    width: 60px; height: 100px;
    background: var(--decor);
  }
</style>
</head>
<body>

<div class="dieline">
  <section class="panel panel--side">
    <div class="side-copy">
      <h2>Elit, sed do eiusmod tempor incididunt ut labore et dolore magna aliqua.</h2>
      <p>Steeped from hand-picked black leaves and sun-dried daisy petals, this blend pours a bright amber cup with a soft floral finish and a cool breath of fresh mint.</p>
      <p>Bring fresh water to a rolling boil, pour over one bag and steep for three to five minutes. Enjoy plain or with a slice of lemon and a little honey.</p>
      <ul class="features">
        <li>Twenty bags of whole leaf tea</li>
        <li>Grown on small family gardens</li>
        <li>Packed in fully recyclable paper</li>
        <li>Best before date on base</li>
      </ul>
      <div class="sponsors-label">Your sponsors:</div>
      <div class="sponsors">
        <span class="sponsor sponsor--round"></span>
        <span class="sponsor"></span>
        <span class="sponsor sponsor--round"></span>
        <span class="sponsor"></span>
      </div>
      <div class="fine-print">Store in a cool, dry place away from strong odours and light.</div>
    </div>
    <div class="rule rule--upper"></div>
    <div class="footer-line">copperferntea.com</div>
    <div class="rule rule--lower"></div>
    <div class="band"></div>
  </section>

  <section class="panel panel--front">
    <div class="cup-mark">
      <svg width="40" height="28" viewBox="0 0 40 28" aria-hidden="true">
        <path d="M6 6 H28 V14 A11 11 0 0 1 6 14 Z" fill="none" stroke="#9a9da0" stroke-width="2"/>
        <path d="M28 9 H32 A4 4 0 0 1 32 17 H27" fill="none" stroke="#9a9da0" stroke-width="2"/>
        <line x1="2" y1="26" x2="34" y2="26" stroke="#9a9da0" stroke-width="2"/>
      </svg>
      <div>Great tea</div>
    </div>

    <div class="brand">
      <span class="brand-dot"></span>
      <span>Copper Fern<br>Tea Company</span>
    </div>

    <div class="variety">Black Tea with<br>Daisy &amp; Meant</div>

    <div class="photo-window" role="img" aria-label="Photo of white chamomile daisies in a green meadow, shown through a leaf-shaped window"></div>
    <div class="corner-decor" role="img" aria-label="Faint decorative tea leaves"></div>

    <div class="rule rule--upper"></div>
    <div class="footer-line slogan">Lorem ipusim your slogan</div>
    <div class="rule rule--lower"></div>
    <div class="band"></div>
  </section>
</div>

<div class="meadow" role="img" aria-label="Photo of white daisies with yellow centres across a green meadow"></div>

</body>
</html>
```